Electrical business needs a flyer design

we need a Trifold flyer designed for an electrical company. Our service include new installations, renovations and rewires, safety checks, switchboard upgrades, services and breakdown, home automation and power monitoring. we would like to see designs using dark grey, orange and blue. the final designs should communicate a friendly but professional service. I have attached my old business brochure to indicate the service we provide
Target Market(s)
home owners
Industry/Entity Type
Electrical
Look and feel
Each slider illustrates characteristics of the customer's brand and the style your logo design should communicate.

```html
<!DOCTYPE html>
<html lang="en">
<head>
<meta charset="utf-8">
<title>Kestrel Line Electrical – Services Flyer</title>
<link rel="stylesheet" href="https://fonts.googleapis.com/css2?family=Roboto+Condensed:wght@300;400;500;700&display=swap">
<style>
  :root {
    --orange: #f07223;
    --blue: #0a8fce;
    --blue-text: #0b8fd0;
    --white: #ffffff;
    --ink: #2b2f33;
    --photo-dark: #1d2733;
    --photo-light: #c9d3db;
  }
  * { box-sizing: border-box; margin: 0; padding: 0; }
  html, body { width: 1200px; height: 848px; overflow: hidden; background: var(--white); }
  body { font-family: "Roboto Condensed", Arial, sans-serif; }
  .flyer { position: relative; width: 1200px; height: 848px; background: var(--white); overflow: hidden; }
  .block { position: absolute; }

  .photo-switchboard {
    left: 0; top: 0; width: 674px; height: 404px;
    background: radial-gradient(ellipse at 55% 45%, #d9dee3 0%, #9aa8b4 35%, #3a4a5c 70%, var(--photo-dark) 100%);
  }
  .photo-technician {
    left: 808px; top: 274px; width: 392px; height: 574px;
    background: linear-gradient(160deg, #8fa6b8 0%, var(--photo-light) 40%, #d8c0ad 65%, #aab8c4 100%);
  }

  .service-banner {
    left: 481px; top: 152px; width: 327px; height: 122px;
    background: var(--orange);
    display: flex; align-items: center; padding-left: 13px;
  }
  .service-banner h2 {
    color: var(--white); font-weight: 500; font-size: 55px; letter-spacing: 0.5px; line-height: 1;
  }

  .philosophy {
    left: 808px; top: 0; width: 392px; height: 274px;
    background: var(--orange); color: var(--white);
    padding: 14px 0 0 14px;
  }
  .philosophy h2 {
    font-weight: 500; font-size: 48px; line-height: 1; letter-spacing: 0.5px;
    padding-bottom: 8px; border-bottom: 2px solid var(--white); width: 358px;
  }
  .philosophy p {
    font-weight: 400; font-size: 19.5px; line-height: 22.4px; margin-top: 13px; padding-left: 6px; width: 360px;
  }

  .electrical {
    left: 0; top: 404px; width: 404px; height: 444px;
    background: var(--blue); color: var(--white); padding: 20px 0 0 21px;
  }
  .electrical h3 { font-weight: 500; font-size: 46px; line-height: 1; }

  .communication {
    left: 404px; top: 404px; width: 404px; height: 343px;
    background: var(--white); color: var(--blue-text); padding: 22px 0 0 19px;
  }
  .communication h3 { font-weight: 700; font-size: 47px; line-height: 49px; }

  .service-list { list-style: none; }
  .service-list li { display: flex; align-items: center; font-size: 21.5px; font-weight: 400; }
  .electrical .service-list { margin-top: 16px; }
  .electrical .service-list li { height: 47px; }
  .communication .service-list { margin-top: -6px; }
  .communication .service-list li { height: 53.5px; }

  .icon {
    width: 42px; height: 42px; border-radius: 50%; flex: none; margin-right: 10px;
    display: flex; align-items: center; justify-content: center;
  }
  .electrical .icon { background: var(--white); width: 40px; height: 40px; }
  .communication .icon { border: 2px solid var(--orange); }
  .icon svg { width: 24px; height: 24px; }

  .cta {
    left: 404px; top: 747px; width: 404px; height: 101px;
    background: var(--blue); color: var(--white); text-align: center;
  }
  .cta-title { display: flex; align-items: center; justify-content: center; gap: 10px; margin-top: 11px; }
  .cta-title .phone-number { font-weight: 500; font-size: 42px; line-height: 1; letter-spacing: 0.5px; }
  .cta-title svg { width: 34px; height: 34px; }
  .cta-quote { font-size: 19px; line-height: 22px; margin-top: 5px; }
  .cta-email { font-size: 16px; line-height: 19px; font-weight: 300; }
</style>
</head>
<body>
<main class="flyer">
  <div class="block photo-switchboard" role="img" aria-label="Photo of an electrician testing a circuit breaker switchboard with coloured wiring"></div>

  <div class="block service-banner"><h2>OUR SERVICE</h2></div>

  <section class="block philosophy">
    <h2>OUR PHILOSOPHY</h2>
    <p>Kestrel Line Electrical focuses on providing our customers with the best possible service available. Our trades people are highly qualified to ensure quality and reliability. We strive to continually change and grow within the industry.<br>We are consantly making changes to serve you better.</p>
  </section>

  <div class="block photo-technician" role="img" aria-label="Photo of hands using an orange screwdriver on a wiring panel"></div>

  <section class="block electrical">
    <h3>Electrical service</h3>
    <ul class="service-list">
      <li><span class="icon"><svg viewBox="0 0 26 26" fill="none" stroke="#f07223" stroke-width="3" stroke-linecap="round"><path d="M13 3v20M3 13h20"/></svg></span>New installations</li>
      <li><span class="icon"><svg viewBox="0 0 26 26" fill="none" stroke="#f07223" stroke-width="3" stroke-linecap="round"><path d="M5 21l9-9M16 4a5 5 0 0 0 6 6l-3-1-2-2z"/><path d="M5 5l4 4M9 9l12 12"/></svg></span>Renovations and re-wiring</li>
      <li><span class="icon"><svg viewBox="0 0 26 26" fill="none" stroke="#f07223" stroke-width="2.2" stroke-linejoin="round"><path d="M2 12L13 3l11 9M5 10v13h16V10"/><circle cx="13" cy="16" r="4.5"/><path d="M14 13l-2 3h2l-2 3"/></svg></span>Installation of safety switches</li>
      <li><span class="icon"><svg viewBox="0 0 26 26" fill="#f07223"><path d="M13 2l9 11h-5v11h-8V13H4z"/></svg></span>Switchboard upgrades</li>
      <li><span class="icon"><svg viewBox="0 0 26 26" fill="none" stroke="#f07223" stroke-width="3" stroke-linecap="round"><path d="M5 21l9-9M16 4a5 5 0 0 0 6 6l-3-1-2-2z"/><path d="M5 5l4 4M9 9l12 12"/></svg></span>Services and breakdowns</li>
      <li><span class="icon"><svg viewBox="0 0 26 26" fill="none" stroke="#f07223" stroke-width="2.2" stroke-linejoin="round"><path d="M2 12L13 3l11 9M5 10v13h16V10"/><path d="M10 17h6M13 14v6"/></svg></span>Home automation</li>
      <li><span class="icon"><svg viewBox="0 0 26 26" fill="none" stroke="#f07223" stroke-width="2.2" stroke-linecap="round"><path d="M4 18a9 9 0 0 1 18 0"/><path d="M13 18l5-6"/><circle cx="13" cy="18" r="1.6" fill="#f07223"/></svg></span>Power monitoring</li>
    </ul>
  </section>

  <section class="block communication">
    <h3>Communication<br>service</h3>
    <ul class="service-list">
      <li><span class="icon"><svg viewBox="0 0 26 26" fill="none" stroke="#0b8fd0" stroke-width="3" stroke-linecap="round"><path d="M13 3v20M3 13h20"/></svg></span>New installations</li>
      <li><span class="icon"><svg viewBox="0 0 26 26" fill="none" stroke="#0b8fd0" stroke-width="2"><circle cx="5" cy="20" r="2.5"/><circle cx="10" cy="10" r="2.5"/><path d="M6 18l3-6M12 11l3 5"/><circle cx="18" cy="17" r="5"/><path d="M18 14v6M15 17h6"/></svg></span>Additional phone and data points</li>
      <li><span class="icon"><svg viewBox="0 0 26 26" fill="none" stroke="#0b8fd0" stroke-width="2.2"><rect x="3" y="5" width="20" height="13" rx="1"/><path d="M13 18v4M8 22h10"/></svg></span>Antennas and TV points</li>
      <li><span class="icon"><svg viewBox="0 0 26 26" fill="none" stroke="#0b8fd0" stroke-width="2.5" stroke-linecap="round"><path d="M3 10a14 14 0 0 1 20 0M6.5 13.5a9 9 0 0 1 13 0M10 17a4 4 0 0 1 6 0"/><circle cx="13" cy="20.5" r="1.5" fill="#0b8fd0"/></svg></span>LAN setups</li>
    </ul>
  </section>

  <section class="block cta">
    <div class="cta-title">
      <svg viewBox="0 0 36 36" fill="#ffffff"><path d="M8 4l5 7-3 3c2 5 6 9 11 11l3-3 7 5-3 5C16 32 4 20 3 7z"/><path d="M20 6a10 10 0 0 1 10 10M20 11a5 5 0 0 1 5 5" fill="none" stroke="#ffffff" stroke-width="2"/></svg>
      <span class="phone-number">1300 555 018</span>
    </div>
    <p class="cta-quote">Call us today for a free no obligation quote</p>
    <p class="cta-email">hello@kestrelline.com.au</p>
  </section>
</main>
</body>
</html>
```